Business card design for holistic health care clinic

We need a double-sided business card design for our holistic health care clinic that integrates our logo design and also its color scheme. My business is called Veluma. It is an integrative medicine clinic. You have already done the logo for me. Please ensure an elegant and upscale design that is not cluttered, but still has all the necessary information (please see below for details).

Target Market(s)

Wellness, fitness, rehabilitation for educated, well-traveled open-minded clients who are focused on natural, organic, balanced and preventive healthcare and lifestyle.

Industry/Entity Type

Medical

Contact Information for Business Card

Modern, clean.

Number of Pages Required

1 page

Font styles to use
Serif
Sans Serif

Colors

Designer to choose colors to be used in the design.

Requirements
Must have
• Logo on one side, all other information on the other side.
• Other information should include:
• Tomas Brevik - DOE, CPT, LMT
• 4120 North Harlow Street
• Austin, TX 78631
• 512 608 2947
• 818 459 7208
• info@VelumaHealth.com
• t.brevik@VelumaHealth.com
Nice to have
• Darker background on front - but not totally black - shaded/dark gray.

```html
<!DOCTYPE html>
<html lang="en">
<head>
<meta charset="utf-8">
<title>Veluma – Business Card</title>
<link href="https://fonts.googleapis.com/css2?family=Montserrat:wght@400;500;600;800&display=swap" rel="stylesheet">
<style>
  :root {
    --stage: #1f1f21;
    --brand-blue: #1c8fcf;
    --brand-blue-light: #2ea3e0;
    --card-dark: #2a2a2c;
    --card-dark-edge: #232325;
    --ink-light: #e9ecef;
    --ink-muted: #b9c0c6;
    --band-edge: #141416;
  }
  * { box-sizing: border-box; margin: 0; padding: 0; }
  html, body {
    width: 1200px; height: 900px; overflow: hidden;
    background: var(--stage);
    font-family: "Montserrat", Arial, sans-serif;
  }
  .sheet {
    width: 1200px; height: 900px;
    display: flex; flex-direction: column; align-items: center; justify-content: center;
    gap: 56px;
  }
  .card {
    position: relative;
    width: 660px; height: 377px;
    border-radius: 4px;
    overflow: hidden;
    box-shadow: 0 14px 30px rgba(0,0,0,.45);
  }

  /* Logo side */
  .card--logo {
    background: var(--brand-blue);
    color: #fff;
    display: flex; flex-direction: column; align-items: center; justify-content: center;
  }
  .wordmark {
    display: flex; align-items: center; gap: 14px;
  }
  .wordmark__dot {
    width: 22px; height: 22px; border-radius: 50%;
    background: currentColor;
  }
  .wordmark__name {
    font-weight: 800;
    font-size: 64px;
    letter-spacing: 2px;
    line-height: 1;
  }
  .tagline-main {
    margin-top: 8px;
    font-weight: 600;
    font-size: 19px;
    letter-spacing: .5px;
  }
  .motto {
    margin-top: 34px;
    display: flex; align-items: center; gap: 12px;
    font-size: 14px; font-weight: 500; font-style: normal;
  }
  .motto__rule {
    width: 150px; height: 1px; background: rgba(255,255,255,.75);
  }

  /* Info side */
  .card--info {
    background: linear-gradient(135deg, var(--card-dark) 0%, var(--card-dark-edge) 100%);
    color: var(--ink-light);
  }
  .band {
    position: absolute; left: 0; top: 0; width: 250px; height: 100%;
  }
  .band__url {
    position: absolute;
    left: 36px; bottom: 24px;
    transform-origin: left bottom;
    transform: rotate(-90deg) translateY(100%);
    color: #fff;
    font-weight: 600; font-size: 17px; letter-spacing: 1px;
    white-space: nowrap;
  }
  .info {
    position: absolute; left: 290px; top: 40px; right: 30px;
  }
  .info .wordmark { color: var(--brand-blue-light); }
  .info .wordmark__name { font-size: 48px; }
  .info .wordmark__dot { width: 16px; height: 16px; }
  .info .tagline-main {
    color: var(--brand-blue-light); font-size: 14px; margin-top: 6px;
  }
  .person { margin-top: 28px; }
  .person__name {
    color: var(--brand-blue-light);
    font-weight: 600; font-size: 19px; letter-spacing: 1px; text-transform: uppercase;
  }
  .person__creds {
    color: var(--brand-blue-light);
    font-size: 11px; font-weight: 500; letter-spacing: 1px; margin-top: 2px;
  }
  .contact {
    margin-top: 14px; list-style: none;
    font-size: 14px; line-height: 1.55; color: var(--ink-light);
  }
  .contact__label { color: var(--brand-blue-light); font-weight: 600; margin-right: 4px; }
</style>
</head>
<body>
<main class="sheet">

  <section class="card card--logo" aria-label="Card front">
    <div class="wordmark">
      <span class="wordmark__dot"></span>
      <span class="wordmark__name">VELUMA</span>
    </div>
    <p class="tagline-main">Integrative Holistic Medicine</p>
    <p class="motto">
      <span class="motto__rule"></span>
      <span>helping the body help itself</span>
      <span class="motto__rule"></span>
    </p>
  </section>

  <section class="card card--info" aria-label="Card back">
    <svg class="band" viewBox="0 0 250 377" preserveAspectRatio="none" aria-hidden="true">
      <path d="M0 0 H105 C210 70 240 200 200 290 C185 325 175 350 180 377 H0 Z"
            fill="var(--band-edge)"/>
      <path d="M0 0 H92 C192 70 222 200 184 290 C170 325 160 350 164 377 H0 Z"
            fill="var(--brand-blue)"/>
    </svg>
    <span class="band__url">www.VelumaHealth.com</span>

    <div class="info">
      <div class="wordmark">
        <span class="wordmark__name">VELUMA</span>
        <span class="wordmark__dot"></span>
      </div>
      <p class="tagline-main">Integrative Holistic Medicine</p>

      <div class="person">
        <p class="person__name">Tomas Brevik</p>
        <p class="person__creds">DOE, CPT, LMT</p>
      </div>

      <ul class="contact">
        <li>4120 North Harlow Street</li>
        <li>Austin, TX 78631</li>
        <li><span class="contact__label">P.</span>512 608 2947</li>
        <li><span class="contact__label">C.</span>818 459 7208</li>
        <li>t.brevik@VelumaHealth.com</li>
      </ul>
    </div>
  </section>

</main>
</body>
</html>
```